Landing Page für Freelancer im Bereich der Informationstechnik
Zielgruppe
Ich bin Experte für Informationstechnik, Unified Communications, Beratung, Management sowie Projekte aller Art.
Mit meiner WOLKENTOR GmbH bin ich als (einzelner) Freelancer für mittelständische Unternehmen und Konzerne in verschiedensten Projekten tätig.
Mein Motto lautet 'Mit Präzision und langjähriger Erfahrung immer alles im Griff!'
Aufgabenstellung
Die aktuell existierende Internet-Präsenz unter wolkentor-web.de beinhaltet aktuell nur eine minimalistische statische Seite sowie das Impressum, ohne jegliche dynamische Inhalte.
DABEI SOLL ES BLEIBEN. Auch die Inhalte sollen unverändert übernommen werden.
Lediglich soll jetzt eine Anlehnung an das zwischenzeitlich vorhandene Logo vorgenommen werden, welches ich mitliefere.
Es geht mir insgesamt nur darum, ein professionelleres Auftreten zu haben, WENN sich denn mal jemand auf die Seite verirrt.
Das Aussehen soll daher modern und dynamisch sein.
ZUSAMMENFASSUNG: Inhalte bleiben 1:1, grafische Anpassung an Logo gewünscht.
Technisch: Statisch, kein Content-Management. Lohnt sich hier nicht.
SEHR WICHTIG: Ich möchte gerne, dass die Lieferung bereits als HTML (und NICHT NUR ALS GRAFIK) erfolgt, ggf. stelle ich auch kurz den FTP-Zugang.
Insgesamt möchte ich gar keine große Sache draus machen.
Viele Anpassungsrunden wird es voraussichtlich nicht geben.
Zeitlich ist dies hier ein sehr kleines Projekt - Erweiterungen kommen später.

```html
<!DOCTYPE html>
<html lang="de">
<head>
<meta charset="utf-8">
<title>Mirko Andreas Falk – WOLKENTOR GmbH</title>
<link href="https://fonts.googleapis.com/css2?family=Outfit:wght@400;500;600&display=swap" rel="stylesheet">
<style>
  :root {
    --teal: #55a7c0;
    --ink: #3b3b3d;
    --paper: #ffffff;
    --wood-light: #ece2d4;
    --wood-mid: #dccdb8;
    --line: #9fcfdd;
  }
  * { margin: 0; padding: 0; box-sizing: border-box; }
  html, body { width: 1047px; height: 1200px; overflow: hidden; background: var(--paper); }
  body { position: relative; font-family: "Outfit", sans-serif; color: var(--ink); }

  .site-nav { position: absolute; top: 88px; left: 101px; display: flex; gap: 37px; }
  .site-nav a { font-size: 12.5px; font-weight: 500; color: var(--ink); text-decoration: none; }

  .brand {
    position: absolute; top: 128px; left: 764px; width: 170px;
    text-align: center; color: var(--teal); font-weight: 600;
    font-size: 17px; letter-spacing: 1.5px;
  }

  .intro { position: absolute; left: 101px; top: 203px; }
  .intro__degree { font-size: 21px; font-weight: 600; line-height: 1; }
  .intro__name { margin-top: 22px; font-size: 40px; font-weight: 600; color: var(--teal); line-height: 1; letter-spacing: -0.3px; }
  .intro__master { margin-top: 22px; font-size: 21px; font-weight: 600; line-height: 1; }

  .contact-link {
    position: absolute; left: 101px; top: 418px;
    font-size: 12px; font-weight: 500; color: var(--ink); text-decoration: none;
    border-bottom: 1px solid var(--line); padding-bottom: 1px;
  }

  .services { position: absolute; left: 426px; top: 413px; width: 520px; }
  .services__title { font-size: 29px; font-weight: 600; line-height: 39px; letter-spacing: -0.2px; }
  .services__text { margin-top: 25px; font-size: 11.4px; font-weight: 500; line-height: 18px; }

  .feature { position: absolute; left: 101px; top: 682px; width: 845px; height: 423px; display: flex; }
  .feature__motto {
    width: 326px; height: 100%; background: var(--teal); color: var(--paper);
    display: flex; flex-direction: column; align-items: center;
  }
  .feature__brand { margin-top: 140px; font-size: 15px; font-weight: 600; letter-spacing: 1.3px; }
  .feature__quote {
    margin-top: 50px; text-align: center; font-size: 17.5px; font-weight: 600;
    line-height: 27px; text-transform: uppercase; letter-spacing: -0.2px;
  }
  .feature__photo {
    flex: 1; height: 100%;
    background: linear-gradient(135deg, var(--wood-light) 0%, var(--wood-mid) 100%);
  }
</style>
</head>
<body>
  <nav class="site-nav">
    <a href="#">Startseite</a>
    <a href="#">Impressum</a>
    <a href="#">Datenschutz</a>
  </nav>

  <div class="brand">WOLKENTOR GmbH</div>

  <header class="intro">
    <p class="intro__degree">Diplom-Informatiker (FH)</p>
    <h1 class="intro__name">Mirko Andreas Falk</h1>
    <p class="intro__master">Master of Science in Electronic Business</p>
  </header>

  <a class="contact-link" href="#">m punkt falk at wolkentor-web punkt de</a>

  <section class="services">
    <h2 class="services__title">Experte für Informationstechnik | Unified Communications | Beratung | Management | Projekte aller Art</h2>
    <p class="services__text">Gerne schicke ich Ihnen unverbindlich mein Expertenprofil samt CV sowie meine aktuellen Verfügbarkeiten zu. Kontaktieren Sie mich hierzu einfach per E-Mail unter m punkt falk at wolkentor-web punkt de. Ich freue mich auf Sie!</p>
  </section>

  <section class="feature">
    <div class="feature__motto">
      <div class="feature__brand">WOLKENTOR GmbH</div>
      <p class="feature__quote">"Mit Präzision<br>und langjähriger<br>Erfahrung immer<br>alles im Griff!"</p>
    </div>
    <div class="feature__photo" role="img" aria-label="Foto von oben auf einen Holztisch mit mehreren Laptops, Smartphones, Teekanne und Händen bei der Arbeit"></div>
  </section>
</body>
</html>
```